Awesome Office Furniture Dealer's Brochure!

Need a professional and informative brochure put together for our clients - may need separate designs for Government and Education clients. Should be based of our new website design and feel. Sections should include: Manufacturers we carry, services, and statements about our company - who we are & what we do. Brochure is 8.5 x 11 in tri-fold configuration. Template files attached.

Target Market(s)

Small to Medium businesses

Industry/Entity Type

Office Furniture

Requirements
Must have
• Look and feel of our website www.pelmaro.com. Images can be taken from any of our vendors listed under /products, look to VEX primarily. We will get the final designer production ready images when needed.
Nice to have
• Incorporate the "love your workspace" from our website.

```html
<!DOCTYPE html>
<html lang="en">
<head>
<meta charset="utf-8">
<title>Pelmaro Office Furniture – Tri-fold Brochure</title>
<link href="https://fonts.googleapis.com/css2?family=Montserrat:wght@500;600;700&family=Questrial&family=Kaushan+Script&display=swap" rel="stylesheet">
<style>
  :root{
    --green:#6cc13a;
    --green-light:#8ad64b;
    --green-dark:#4e9e25;
    --grey:#6b6b6d;
    --grey-light:#e9e9e9;
    --ink:#2a2a2a;
    --paper:#ffffff;
    --backdrop:#d9d9d9;
  }
  *{box-sizing:border-box;margin:0;padding:0}
  html,body{width:1200px;height:1200px;overflow:hidden;background:var(--backdrop)}
  body{position:relative;font-family:"Questrial",sans-serif;color:var(--ink)}
  .brochure{position:absolute;left:50px;top:175px;width:1100px;height:850px;display:flex;background:var(--paper);box-shadow:0 10px 30px rgba(0,0,0,.18)}
  .panel{position:relative;width:366.67px;height:100%;overflow:hidden;background:linear-gradient(180deg,#fff 0%,#f4f4f4 60%,#fff 100%)}
  .panel + .panel{border-left:1px solid #e3e3e3}
  .panel svg.art{position:absolute;left:0;top:0}
  .band{position:absolute;left:0;bottom:0;width:100%;height:48px}
  .band--green{background:var(--green)}
  .band--grey{background:var(--grey)}

  /* left panel */
  .services{position:absolute;left:36px;top:268px;right:30px}
  .services h2{font-family:"Montserrat",sans-serif;font-weight:600;color:var(--green);font-size:26px;margin-bottom:8px}
  .services p{font-size:13.5px;line-height:1.4;color:#444}
  .checklist{list-style:none;margin-top:16px}
  .checklist li{display:flex;align-items:center;gap:8px;font-family:"Montserrat",sans-serif;font-weight:600;color:var(--green);font-size:15px;line-height:1.55}
  .checklist svg{flex:none}
  .photo-frame{position:absolute;left:46px;top:500px;width:276px;height:156px;border:5px solid var(--green);background:linear-gradient(135deg,#e6dccb,#c9b79a 55%,#5a6fa8)}
  .used{position:absolute;left:40px;top:690px;right:26px}
  .used h3{font-family:"Montserrat",sans-serif;font-weight:600;color:var(--green);font-size:13.5px;line-height:1.35;text-transform:uppercase}
  .used p{margin-top:12px;font-size:13.5px;line-height:1.4;color:#444}

  /* middle panel */
  .screen{position:absolute;left:96px;top:52px;width:178px;height:118px}
  .why{position:absolute;left:30px;right:30px;top:290px;text-align:center}
  .why h2{font-family:"Montserrat",sans-serif;font-weight:600;color:var(--green-dark);font-size:19px}
  .pill{display:inline-block;margin-top:10px;background:var(--green-dark);color:#fff;font-family:"Montserrat",sans-serif;font-weight:500;font-size:11.5px;padding:5px 14px;border-radius:14px}
  .why p{margin-top:24px;font-size:12.5px;line-height:1.5;color:#444;text-align:justify;text-align-last:center}
  .divider{display:block;margin:28px auto 0}
  .contact{position:absolute;left:20px;right:20px;top:600px;text-align:center}
  .contact h2{font-family:"Kaushan Script",cursive;font-weight:400;color:var(--green-dark);font-size:40px;margin-bottom:10px}
  .contact p{font-size:14px;line-height:1.7;color:#222}
  .contact .phone{color:var(--green-dark);font-size:19px}

  /* right panel */
  .brand{position:absolute;left:60px;top:58px;display:flex;align-items:center;gap:12px}
  .brand-dot{width:34px;height:34px;border-radius:50%;background:var(--grey)}
  .brand-name{font-family:"Montserrat",sans-serif;font-weight:600;font-size:36px;color:var(--green);letter-spacing:1px}
  .tagline{position:absolute;left:0;right:0;top:470px;font-family:"Kaushan Script",cursive;font-size:46px;line-height:1.15;color:var(--ink);padding-left:40px}
  .tagline span{display:block;padding-left:36px;color:var(--green-dark)}
  .right-divider{position:absolute;left:118px;top:608px}
  .url{position:absolute;left:0;right:0;top:648px;text-align:center;font-size:15px;letter-spacing:1.5px;color:#333}
</style>
</head>
<body>
<main class="brochure">

  <section class="panel panel--services">
    <svg class="art" width="367" height="850" viewBox="0 0 367 850">
      <defs>
        <clipPath id="office-clip"><path d="M0 0H367V190C300 205 260 180 190 195C120 210 60 250 0 262Z"/></clipPath>
      </defs>
      <g role="img" aria-label="Photo of an open-plan office with desks and colourful chairs">
        <rect width="367" height="270" fill="url(#office-fill)" clip-path="url(#office-clip)"/>
      </g>
      <linearGradient id="office-fill" x1="0" y1="0" x2="1" y2="1">
        <stop offset="0" stop-color="#e7ecea"/><stop offset=".6" stop-color="#d2d8d6"/><stop offset="1" stop-color="#c9cfcd"/>
      </linearGradient>
      <path d="M0 262C60 250 120 210 190 195C260 180 300 205 367 190V200C300 215 262 190 192 205C122 220 62 262 0 274Z" fill="var(--grey)"/>
    </svg>
    <div class="services">
      <h2>Services</h2>
      <p>From initial space-planning to final installation, Pelmaro can help with every phase of your project.</p>
      <ul class="checklist">
        <li><svg width="11" height="11" viewBox="0 0 11 11"><circle cx="5.5" cy="5.5" r="5.5" fill="var(--green)"/><path d="M3 5.6L4.8 7.3L8 3.9" stroke="#fff" stroke-width="1.5" fill="none"/></svg>SPACE PLANNING</li>
        <li><svg width="11" height="11" viewBox="0 0 11 11"><circle cx="5.5" cy="5.5" r="5.5" fill="var(--green)"/><path d="M3 5.6L4.8 7.3L8 3.9" stroke="#fff" stroke-width="1.5" fill="none"/></svg>DESIGN</li>
        <li><svg width="11" height="11" viewBox="0 0 11 11"><circle cx="5.5" cy="5.5" r="5.5" fill="var(--green)"/><path d="M3 5.6L4.8 7.3L8 3.9" stroke="#fff" stroke-width="1.5" fill="none"/></svg>RENDER</li>
        <li><svg width="11" height="11" viewBox="0 0 11 11"><circle cx="5.5" cy="5.5" r="5.5" fill="var(--green)"/><path d="M3 5.6L4.8 7.3L8 3.9" stroke="#fff" stroke-width="1.5" fill="none"/></svg>DELIVERY &amp; INSTALLATION</li>
      </ul>
    </div>
    <div class="photo-frame" role="img" aria-label="Photo of movers carrying a sofa among cardboard boxes"></div>
    <div class="used">
      <h3>Pelmaro has a rotating selection of quality used furniture.</h3>
      <p>Stop by a Pelmaro location<br>To see everything.</p>
    </div>
    <div class="band band--green"></div>
  </section>

  <section class="panel panel--about">
    <svg class="art" width="367" height="850" viewBox="0 0 367 850">
      <path d="M0 0H367V170C300 205 250 250 170 230C100 212 50 190 0 205Z" fill="var(--green-light)"/>
      <path d="M0 205C50 190 100 212 170 230C250 250 300 205 367 170V184C300 222 248 264 168 244C98 226 50 204 0 218Z" fill="var(--grey)"/>
    </svg>
    <svg class="screen" viewBox="0 0 178 118" role="img" aria-label="Laptop illustration displaying a sustainability award badge">
      <rect x="12" y="0" width="154" height="104" rx="6" fill="#222"/>
      <rect x="20" y="8" width="138" height="88" fill="#fff"/>
      <circle cx="89" cy="50" r="24" fill="var(--green)"/>
      <rect x="0" y="104" width="178" height="9" rx="3" fill="#cfcfcf"/>
    </svg>
    <div class="why">
      <h2>Why Pelmaro office furniture?</h2>
      <span class="pill">Because we make buying office furniture easy.</span>
      <p>First, we know what we are doing. With over 30 years of experience in commercial furniture, you can count on our knowledgeable staff to help you through the entire buying process from design to product choice to final installation.</p>
      <svg class="divider" width="110" height="16" viewBox="0 0 110 16">
        <path d="M2 8H104M98 3L106 8L98 13M2 4L8 8L2 12M8 4L14 8L8 12" stroke="var(--grey)" stroke-width="1.5" fill="none"/>
        <circle cx="55" cy="8" r="6" fill="var(--green)"/>
      </svg>
    </div>
    <div class="contact">
      <h2>Contact Us</h2>
      <p>418 Alder Row, Brightwater, WA 98000</p>
      <p>Email: info@pelmaro.com</p>
      <p class="phone">Call: 555.014.2290</p>
    </div>
    <div class="band band--grey"></div>
  </section>

  <section class="panel panel--cover">
    <svg class="art" width="367" height="850" viewBox="0 0 367 850">
      <path d="M0 0C20 90 90 150 200 160C290 168 340 190 367 220V232C330 200 280 180 190 176C80 166 20 110 0 30Z" fill="var(--green)"/>
      <path d="M0 180C80 178 150 190 220 200C290 210 340 220 367 240V440C300 470 230 430 160 445C90 460 40 470 0 470Z" fill="#b9b1a8" role="img" aria-label="Photo of a lounge area with red chairs and a white sofa"/>
      <path d="M0 470C40 470 90 460 160 445C230 430 300 470 367 440V458C300 490 232 450 162 465C92 480 40 490 0 490Z" fill="var(--green)"/>
    </svg>
    <div class="brand"><span class="brand-dot"></span><span class="brand-name">PELMARO</span></div>
    <div class="tagline">Love your<span>workspace!</span></div>
    <svg class="right-divider" width="120" height="16" viewBox="0 0 120 16">
      <path d="M2 8H114M108 3L116 8L108 13M2 4L8 8L2 12M8 4L14 8L8 12" stroke="var(--grey)" stroke-width="1.5" fill="none"/>
      <circle cx="60" cy="8" r="6" fill="var(--green)"/>
    </svg>
    <div class="url">www.pelmaro.com</div>
    <div class="band band--green"></div>
  </section>

</main>
</body>
</html>
```